A clean crisp business card for a Landscape Construction company. Designed to be easy to read contact/ info and also be appealing/interesting, unlike a traditional business card.

Industry/Entity Type

Landscape Construction

Contact Information for Business Card

Company name : Bramblecrest Landscape Construction, phone number: (877) 62Vales, website:Bramblecrestlandscapes.example, Email, sales@bramblecrestlandscapes.example

Requirements
Nice to have
• Luxurious finishes/ details…. Icons or emblems next to contact info
Should not have
• Clipart or general pictures

```html
<!DOCTYPE html>
<html lang="en">
<head>
<meta charset="utf-8">
<title>Bramblecrest Landscape Construction – Business Card</title>
<link href="https://fonts.googleapis.com/css2?family=Cinzel:wght@400;600&display=swap" rel="stylesheet">
<style>
  :root {
    --page: #000000;
    --card-blue: #1e72fe;
    --accent-green: #8ef41a;
    --ink: #ffffff;
  }
  * { margin: 0; padding: 0; box-sizing: border-box; }
  html, body { width: 1041px; height: 1200px; overflow: hidden; background: var(--page); }
  body { position: relative; font-family: "Cinzel", Georgia, serif; color: var(--ink); }

  .card { position: absolute; left: 171px; width: 699px; background: var(--card-blue); overflow: hidden; }
  .card-front { top: 200px; height: 375px; }
  .card-back { top: 650px; height: 399px; }

  /* front */
  .front-brand { position: absolute; left: 0; right: 0; top: 218px; text-align: center; }
  .front-brand .brand-name { font-size: 42px; font-weight: 600; letter-spacing: 1px; line-height: 1; }
  .front-brand .brand-tagline { margin-top: 8px; font-size: 14px; letter-spacing: 5px; line-height: 1; }
  .front-rule { position: absolute; left: 0; right: 0; top: 355px; height: 2px; background: var(--ink); }
  .front-band { position: absolute; left: 0; right: 0; top: 359px; height: 16px; display: flex; }
  .front-band .band-blue { flex: 0 0 349px; background: var(--card-blue); }
  .front-band .band-green { flex: 1; background: var(--accent-green); }

  /* back */
  .back-brand { position: absolute; left: 39px; top: 38px; }
  .back-brand .brand-name { font-size: 26px; font-weight: 600; line-height: 1; letter-spacing: 0.5px; }
  .back-brand .brand-tagline { margin-top: 4px; font-size: 8px; letter-spacing: 2.6px; line-height: 1; }

  .holder { position: absolute; left: 43px; top: 148px; }
  .holder-name { font-size: 30px; font-weight: 600; line-height: 1; letter-spacing: 0.5px; }
  .holder-role { margin-top: 8px; font-size: 16px; line-height: 1; }

  .contact-list { position: absolute; left: 43px; top: 240px; list-style: none; }
  .contact-list li { display: flex; align-items: center; height: 20px; margin-bottom: 14px; font-size: 15px; text-transform: lowercase; font-variant: small-caps; }
  .contact-list svg { width: 18px; height: 18px; margin-right: 10px; flex: none; }

  .address { position: absolute; right: 31px; top: 255px; text-align: right; font-size: 15px; line-height: 21px; }
  .address svg { display: block; margin-left: auto; margin-right: 2px; width: 18px; height: 26px; margin-bottom: 6px; }
</style>
</head>
<body>

<section class="card card-front" aria-label="Card front">
  <div class="front-brand">
    <div class="brand-name">Bramblecrest</div>
    <div class="brand-tagline">LANDSCAPE CONSTRUCTION</div>
  </div>
  <div class="front-rule"></div>
  <div class="front-band"><span class="band-blue"></span><span class="band-green"></span></div>
</section>

<section class="card card-back" aria-label="Card back">
  <div class="back-brand">
    <div class="brand-name">Bramblecrest</div>
    <div class="brand-tagline">LANDSCAPE CONSTRUCTION</div>
  </div>

  <div class="holder">
    <div class="holder-name">Avery Holloway</div>
    <div class="holder-role">Construction Manager</div>
  </div>

  <ul class="contact-list">
    <li>
      <svg viewBox="0 0 24 24" aria-hidden="true"><path fill="#fff" d="M6.6 10.8a15.1 15.1 0 0 0 6.6 6.6l2.2-2.2a1 1 0 0 1 1-.25 11.4 11.4 0 0 0 3.6.57 1 1 0 0 1 1 1V20a1 1 0 0 1-1 1A17 17 0 0 1 3 4a1 1 0 0 1 1-1h3.5a1 1 0 0 1 1 1c0 1.25.2 2.45.57 3.57a1 1 0 0 1-.25 1z"/></svg>
      (877) 62Vales
    </li>
    <li>
      <svg viewBox="0 0 24 24" aria-hidden="true"><g fill="none" stroke="#fff" stroke-width="2"><circle cx="12" cy="12" r="10"/><ellipse cx="12" cy="12" rx="4.5" ry="10"/><path d="M2 12h20M4 7h16M4 17h16"/></g></svg>
      Bramblecrestlandscapes.example
    </li>
    <li>
      <svg viewBox="0 0 24 24" aria-hidden="true"><g fill="none" stroke="#fff" stroke-width="2"><rect x="2" y="5" width="20" height="14"/><path d="M2 5l10 8 10-8M2 19l7-7M22 19l-7-7"/></g></svg>
      sales@bramblecrestlandscapes.example
    </li>
  </ul>

  <address class="address" style="font-style:normal">
    <svg viewBox="0 0 18 26" aria-hidden="true"><path fill="#fff" d="M9 0a9 9 0 0 0-9 9c0 6.5 9 17 9 17s9-10.5 9-17a9 9 0 0 0-9-9zm0 12.5A3.5 3.5 0 1 1 9 5.5a3.5 3.5 0 0 1 0 7z"/></svg>
    4170<br>
    Harrow Fen Rd.,<br>
    Suite 204, Millbrook,<br>
    OH 45000
  </address>
</section>

</body>
</html>
```